Verpackungsdesign für Pasta aus Buchweizen
Zielgruppe
Unser Unternehmen GRANOVIK sucht ein sehr modernes Verpackungsdesign für Pasta aus Buchweizen.
Unsere Produkte sind in unserem Online Shop und unterscheiden sich durch die herkömmliche Pasta, da wir Buchweizen in die Verarbeitung mit aufnehmen und somit die gesundheitsfördernde Eigenschaft des Buchweizens im Vordergrund steht. Unsere Pasta aus Buchweizenmehl mit klassischem Hartweizengrieß ist in dieser Form noch nicht im stationären Handel erhältlich, deshalb wünschen wir uns ein neues, ansprechendes Verpackungsdesign welches von den Massenprodukten aus den Regalen im Handel heraussticht. Das Design sollte also minimalistisch und sehr modern wirken, und sich deutlich von der Konkurrenz abheben.
Die Zielgruppe richtet sich sowohl an Massen die Pasta in allen Variationen lieben, als auch an ernährungsbewusste Veganer/Vegetarier die Alternativen im Bereich der herkömmlichen Pasta Kochkultur suchen.
PS: Mit dem Verkauf unserer Pasta investieren wir außerdem in den Aufbau und der Infrastruktur des Erzeugerlandes. Durch unser Prinzip „Teilen & Tragen“ fördern wir mit unseren Gewinnen nachhaltige Projekte in den Erzeugerländern und helfen somit wirtschaftlich benachteiligten Regionen auf der Welt. (Fair Trade)
Aufgabenstellung
Wir besitzen bereits ein Logo und Verpackungen für unsere Pasta Sorten. Das Logo und das Grundgerüst der Stanzform / Verpackungsmaße (inkl. Sichtfenster) soll beibehalten werden (Siehe Anhang). Als Pasta Verpackungen benutzen wir Faltschachteln und Banderolen.
Verpackungsmaße:
- Faltschachtel (90 x 40 x 165 mm)
- Banderole (560 x 70mm)
Der Produktname ist je nach Sorte zu präzisieren:
- Fusilli
- Makkaroni
- Bandnudeln
- Tarhana
Produktgewicht:
- 250g
Eigenschaften:
- Buchweizenmehl
- 100% Vegan
- Kochzeit 3 Minuten
- Liebevolle Handarbeit
WICHTIG:
1) Bitte benutzt die hochgeladene, leere Stanzform für Artwork.
2) Die Designfarbe kann anhand des Aufstellers ausgerichtet werden (CMYK: 0, 20, 32, 0 und 60, 57, 56, 62) es ist aber kein muss und ihr seit frei in der Kreativität.
3) Bitte das Sichtfenster mit Rand wie aktuell auf den Produkten übernehmen (siehe www.granovik.de/shop)
Nach dem Wettbewerb planen wir zusätzlich ein 1zu1 Projekt und würden uns freuen einen Gewinner auszuwählen - Wir freuen uns auf eure Ideen :)

```html
<!DOCTYPE html>
<html lang="de">
<head>
<meta charset="utf-8">
<title>GRANOVIK Buchweizen Pasta – Verpackungen</title>
<link rel="stylesheet" href="https://fonts.googleapis.com/css2?family=Prata&family=Montserrat:wght@400;600&family=Mrs+Saint+Delafield&display=swap">
<style>
  :root {
    --stage: #d3d3d3;
    --carton: #1e1c1c;
    --carton-side: #181616;
    --ink-light: #ffffff;
    --ink-soft: #d9d4d0;
    --band-tarhana: #c59b8f;
    --band-fusilli: #9b6d66;
    --band-makkaroni: #8c5946;
    --window-rim: #f1ddc9;
    --vegan-green: #5a9a3c;
    --script-white: #ffffff;
  }
  * { box-sizing: border-box; margin: 0; padding: 0; }
  html, body {
    width: 1200px;
    height: 3750px;
    overflow: hidden;
    background: var(--stage);
  }
  .pack-scene {
    position: relative;
    width: 1200px;
    height: 1250px;
    overflow: hidden;
  }
  .carton {
    position: absolute;
    left: 210px;
    top: 210px;
    display: flex;
    height: 840px;
  }
  .carton-side {
    position: relative;
    width: 105px;
    height: 100%;
    background: var(--carton-side);
    color: var(--ink-light);
    font-family: "Montserrat", sans-serif;
  }
  .carton-front {
    position: relative;
    width: 420px;
    height: 100%;
    background: var(--carton);
    color: var(--ink-light);
    overflow: hidden;
  }
  .side-title {
    position: absolute;
    left: 16px;
    top: 185px;
    line-height: 1;
  }
  .side-title small { display: block; font-size: 8px; letter-spacing: 0.4px; color: var(--ink-soft); }
  .side-title strong { display: block; font-size: 21px; font-weight: 400; margin-top: 3px; }
  .properties {
    position: absolute;
    left: 12px;
    top: 292px;
    width: 90px;
  }
  .properties h3 { font-size: 11px; font-weight: 600; margin-bottom: 5px; white-space: nowrap; }
  .properties ul { list-style: none; font-size: 6.5px; line-height: 1.8; color: var(--ink-soft); white-space: nowrap; }
  .properties li::before { content: "• "; }
  .vegan-seal {
    position: absolute;
    left: 25px;
    top: 520px;
    width: 54px;
    height: 54px;
    border-radius: 50%;
    background: var(--vegan-green);
    border: 3px solid #ffffff;
  }
  .cooking-drops {
    position: absolute;
    left: 31px;
    top: 720px;
    display: flex;
    gap: 5px;
  }
  .side-weight {
    position: absolute;
    left: 34px;
    top: 756px;
    font-size: 10px;
    color: var(--ink-soft);
  }
  .variety-band {
    position: absolute;
    left: 0;
    top: 410px;
    width: 320px;
    height: 62px;
    z-index: 2;
    display: flex;
    align-items: center;
    padding-left: 165px;
    font-family: "Prata", serif;
    font-size: 20px;
    letter-spacing: 1px;
    color: #1e1c1c;
  }
  .variety-band--tarhana { background: var(--band-tarhana); }
  .variety-band--fusilli { background: var(--band-fusilli); }
  .variety-band--makkaroni { background: var(--band-makkaroni); }
  .brand-mark {
    position: absolute;
    top: 60px;
    left: 0;
    width: 100%;
    display: flex;
    justify-content: center;
    align-items: center;
    gap: 9px;
    font-family: "Prata", serif;
    font-size: 24px;
    letter-spacing: 1px;
  }
  .brand-dot {
    width: 12px;
    height: 12px;
    border-radius: 50%;
    background: var(--ink-light);
  }
  .product-title {
    position: absolute;
    left: 0;
    top: 215px;
    width: 100%;
    text-align: center;
    font-family: "Prata", serif;
    font-weight: 400;
    line-height: 1;
  }
  .product-title .title-grain { display: block; font-size: 32px; letter-spacing: 3px; }
  .product-title .title-main { display: block; font-size: 80px; letter-spacing: 4px; margin-top: 2px; }
  .product-title .title-script {
    position: absolute;
    right: 28px;
    top: 112px;
    font-family: "Mrs Saint Delafield", cursive;
    font-size: 38px;
    letter-spacing: 0;
    white-space: nowrap;
  }
  .pasta-window {
    position: absolute;
    left: 75px;
    top: 525px;
    width: 290px;
    height: 272px;
  }
  .net-weight {
    position: absolute;
    right: 28px;
    bottom: 50px;
    font-family: "Prata", serif;
    font-size: 22px;
    letter-spacing: 1px;
  }
  .scene-script {
    position: absolute;
    left: 772px;
    top: 360px;
    font-family: "Mrs Saint Delafield", cursive;
    font-size: 78px;
    line-height: 0.95;
    color: var(--script-white);
    white-space: nowrap;
  }
  .scene-script span { display: block; padding-left: 14px; }
</style>
</head>
<body>

<svg width="0" height="0" style="position:absolute" aria-hidden="true">
  <defs>
    <linearGradient id="grain-tarhana" x1="0" y1="0" x2="1" y2="1">
      <stop offset="0" stop-color="#c8622e"/>
      <stop offset="1" stop-color="#8a3f22"/>
    </linearGradient>
    <linearGradient id="grain-fusilli" x1="0" y1="0" x2="1" y2="1">
      <stop offset="0" stop-color="#9b6a40"/>
      <stop offset="1" stop-color="#5e3a22"/>
    </linearGradient>
    <linearGradient id="grain-makkaroni" x1="0" y1="0" x2="1" y2="1">
      <stop offset="0" stop-color="#a8714a"/>
      <stop offset="1" stop-color="#6a4028"/>
    </linearGradient>
    <path id="drop" d="M6 0 C9 5 12 8 12 12 A6 6 0 0 1 0 12 C0 8 3 5 6 0 Z" fill="none" stroke="#ffffff" stroke-width="1.6"/>
  </defs>
</svg>

<!-- Tarhana -->
<section class="pack-scene">
  <div class="carton">
    <div class="carton-side">
      <div class="side-title"><small>BUCHWEIZEN</small><strong>PASTA</strong></div>
      <div class="properties">
        <h3>Eigenschaften:</h3>
        <ul><li>Buchweizenmehl</li><li>100% Vegan</li><li>Kochzeit 3 Minuten</li><li>Liebevolle Handarbeit</li></ul>
      </div>
      <div class="vegan-seal"></div>
      <div class="cooking-drops">
        <svg width="12" height="18"><use href="#drop"/></svg>
        <svg width="12" height="18"><use href="#drop"/></svg>
        <svg width="12" height="18"><use href="#drop"/></svg>
      </div>
      <div class="side-weight">250g ℮</div>
    </div>
    <div class="carton-front">
      <div class="brand-mark"><span class="brand-dot"></span>GRANOVIK</div>
      <h1 class="product-title"><span class="title-grain">BUCHWEIZEN</span><span class="title-main">PASTA</span><span class="title-script">Buckwheat</span></h1>
      <svg class="pasta-window" viewBox="0 0 320 300" role="img" aria-label="Sichtfenster mit Tarhana aus Buchweizen">
        <g fill="url(#grain-tarhana)" stroke="var(--window-rim)" stroke-width="6">
          <path d="M205 10 C255 60 250 130 195 170 C150 120 160 55 205 10 Z"/>
          <path d="M10 160 C70 140 135 165 160 210 C110 260 45 240 10 160 Z"/>
          <path d="M130 285 C120 225 165 175 240 170 C245 230 200 275 130 285 Z"/>
        </g>
      </svg>
      <div class="net-weight">250g ℮</div>
    </div>
    <div class="variety-band variety-band--tarhana">tarhana</div>
  </div>
  <p class="scene-script">Buchweizen<span>pasta</span></p>
</section>

<!-- Fusilli -->
<section class="pack-scene">
  <div class="carton">
    <div class="carton-side">
      <div class="side-title"><small>BUCHWEIZEN</small><strong>PASTA</strong></div>
      <div class="properties">
        <h3>Eigenschaften:</h3>
        <ul><li>Buchweizenmehl</li><li>100% Vegan</li><li>Kochzeit 3 Minuten</li><li>Liebevolle Handarbeit</li></ul>
      </div>
      <div class="vegan-seal"></div>
      <div class="cooking-drops">
        <svg width="12" height="18"><use href="#drop"/></svg>
        <svg width="12" height="18"><use href="#drop"/></svg>
        <svg width="12" height="18"><use href="#drop"/></svg>
      </div>
      <div class="side-weight">250g ℮</div>
    </div>
    <div class="carton-front">
      <div class="brand-mark"><span class="brand-dot"></span>GRANOVIK</div>
      <h1 class="product-title"><span class="title-grain">BUCHWEIZEN</span><span class="title-main">PASTA</span><span class="title-script">Buckwheat</span></h1>
      <svg class="pasta-window" viewBox="0 0 320 300" role="img" aria-label="Sichtfenster mit Fusilli aus Buchweizen">
        <g fill="url(#grain-fusilli)" stroke="var(--window-rim)" stroke-width="6">
          <path d="M205 10 C255 60 250 130 195 170 C150 120 160 55 205 10 Z"/>
          <path d="M10 160 C70 140 135 165 160 210 C110 260 45 240 10 160 Z"/>
          <path d="M130 285 C120 225 165 175 240 170 C245 230 200 275 130 285 Z"/>
        </g>
      </svg>
      <div class="net-weight">250g ℮</div>
    </div>
    <div class="variety-band variety-band--fusilli">fusilli</div>
  </div>
  <p class="scene-script">Buchweizen<span>pasta</span></p>
</section>

<!-- Makkaroni -->
<section class="pack-scene">
  <div class="carton">
    <div class="carton-side">
      <div class="side-title"><small>BUCHWEIZEN</small><strong>PASTA</strong></div>
      <div class="properties">
        <h3>Eigenschaften:</h3>
        <ul><li>Buchweizenmehl</li><li>100% Vegan</li><li>Kochzeit 3 Minuten</li><li>Liebevolle Handarbeit</li></ul>
      </div>
      <div class="vegan-seal"></div>
      <div class="cooking-drops">
        <svg width="12" height="18"><use href="#drop"/></svg>
        <svg width="12" height="18"><use href="#drop"/></svg>
        <svg width="12" height="18"><use href="#drop"/></svg>
      </div>
      <div class="side-weight">250g ℮</div>
    </div>
    <div class="carton-front">
      <div class="brand-mark"><span class="brand-dot"></span>GRANOVIK</div>
      <h1 class="product-title"><span class="title-grain">BUCHWEIZEN</span><span class="title-main">PASTA</span><span class="title-script">Buckwheat</span></h1>
      <svg class="pasta-window" viewBox="0 0 320 300" role="img" aria-label="Sichtfenster mit Makkaroni aus Buchweizen">
        <g fill="url(#grain-makkaroni)" stroke="var(--window-rim)" stroke-width="6">
          <path d="M205 10 C255 60 250 130 195 170 C150 120 160 55 205 10 Z"/>
          <path d="M10 160 C70 140 135 165 160 210 C110 260 45 240 10 160 Z"/>
          <path d="M130 285 C120 225 165 175 240 170 C245 230 200 275 130 285 Z"/>
        </g>
      </svg>
      <div class="net-weight">250g ℮</div>
    </div>
    <div class="variety-band variety-band--makkaroni">makkaroni</div>
  </div>
  <p class="scene-script">Buchweizen<span>pasta</span></p>
</section>

</body>
</html>
```